PeZ, Pe Zanith, New fintech for all

New Fintech (Financial Planning and saving goals, cryptoassets custody and exchange, payment processor, discounts in stores).
PeZ, means: Pe Zanith. We will use wearebles for payment cards.
- Iban account (current account)
- Payment card
- Investment account
- Financial Planning, Saving goals and roboadvisor
- Crypto assets exchange and custody
- Shops Offers

Target Market(s)

Young and Middle age. Travelers

Industry/Entity Type

Financial Services

Font styles to use
Other font styles liked:
• Loki cola, American pop, Flanders script, Respect...

Colors

Designer to choose only greyscale colors for use in the design.

Requirements
Must have
• PeZ
Nice to have
• I would like to see black and white tonalities
Should not have
• Colors

```html
<!DOCTYPE html>
<html lang="en">
<head>
<meta charset="UTF-8">
<title>PeZ — Dashboard</title>
<link href="https://fonts.googleapis.com/css2?family=Poppins:wght@300;400;500;600;700&display=swap" rel="stylesheet">
<style>
  :root {
    --canvas: #f7f7f7;
    --screen: #151515;
    --hero-dark: #1c1c1c;
    --hero-mid: #3a3a3a;
    --tile: #2a2a2a;
    --panel: #121212;
    --panel-band: #262626;
    --nav: #1e1e1e;
    --text: #ffffff;
    --text-soft: #bdbdbd;
    --text-dim: #8c8c8c;
    --card-light: #e9e9ea;
    --card-dark: #a7a8ab;
    --ink: #111111;
    --ink-soft: #555555;
    --up: #2fbf5b;
    --down: #e23b3b;
  }
  * { margin: 0; padding: 0; box-sizing: border-box; }
  html, body { width: 1200px; height: 821px; overflow: hidden; background: var(--canvas); }
  body { font-family: 'Poppins', sans-serif; position: relative; }

  .screen {
    position: absolute; left: 424px; top: 30px; width: 351px; height: 760px;
    background: var(--screen); overflow: hidden; color: var(--text);
  }
  .hero-texture {
    position: absolute; left: 0; top: 0; width: 351px; height: 329px;
    background: radial-gradient(ellipse at 60% 35%, var(--hero-mid) 0%, var(--hero-dark) 60%, #161616 100%);
  }
  .abs { position: absolute; }

  .status-time { left: 31px; top: 13px; font-size: 14px; font-weight: 600; }
  .status-icons { right: 16px; top: 16px; }

  .brand { left: 17px; top: 40px; font-size: 30px; font-weight: 500; color: #e4e4e4; letter-spacing: -0.5px; }
  .bell { left: 256px; top: 50px; }
  .badge {
    left: 269px; top: 42px; width: 17px; height: 17px; border-radius: 50%;
    background: #fff; color: var(--ink); font-size: 9px; font-weight: 600;
    display: flex; align-items: center; justify-content: center;
  }
  .avatar {
    left: 303px; top: 47px; width: 31px; height: 31px; border-radius: 50%;
    background: radial-gradient(circle at 50% 40%, #b9b9b9, #6e6e6e);
  }

  .greeting { left: 19px; top: 100px; font-size: 14px; font-weight: 500; }
  .greeting-big { left: 19px; top: 116px; font-size: 20px; font-weight: 700; }

  .card {
    left: 19px; top: 161px; width: 281px; height: 140px; border-radius: 12px;
    background: linear-gradient(135deg, var(--card-light) 0%, #d6d7d9 50%, var(--card-dark) 100%);
    color: var(--ink);
  }
  .card.peek { left: 318px; width: 80px; }
  .card-icon {
    position: absolute; left: 14px; top: 14px; width: 37px; height: 37px; border-radius: 50%;
    background: var(--ink); display: flex; align-items: center; justify-content: center;
  }
  .card-name { position: absolute; left: 65px; top: 16px; font-size: 12.5px; font-weight: 600; }
  .card-type { position: absolute; left: 65px; top: 34px; font-size: 9.5px; color: var(--ink-soft); }
  .card-label { position: absolute; left: 14px; top: 86px; font-size: 9.5px; color: var(--ink-soft); }
  .card-balance { position: absolute; left: 14px; top: 101px; font-size: 17.5px; font-weight: 700; }
  .card-number { position: absolute; right: 14px; top: 105px; font-size: 12px; color: #333; }

  .pager { left: 162px; top: 313px; display: flex; gap: 5px; align-items: center; }
  .pager span { width: 3px; height: 3px; border-radius: 50%; background: #9a9a9a; }
  .pager span.on { width: 5px; height: 5px; background: #fff; }

  .section-title { left: 19px; top: 346px; font-size: 14px; font-weight: 400; display: flex; align-items: center; gap: 9px; }
  .section-title i { width: 13px; height: 13px; border-radius: 50%; background: #d9d9d9; display: block; }

  .tile {
    top: 386px; width: 71px; height: 70px; border-radius: 11px; background: var(--tile);
    display: flex; flex-direction: column; align-items: center; justify-content: center; gap: 5px;
    font-size: 8.5px; color: var(--text-soft); text-align: center; line-height: 1.3;
  }

  .panel {
    left: 19px; top: 475px; width: 314px; height: 230px; border-radius: 11px;
    background: var(--panel); border: 1px solid #2b2b2b;
  }
  .panel-title { position: absolute; left: 14px; top: 17px; font-size: 14px; font-weight: 500; }
  .panel-date { position: absolute; right: 14px; top: 21px; font-size: 10px; color: var(--text-soft); }
  .panel-head {
    position: absolute; left: 0; top: 53px; width: 100%; height: 28px; background: var(--panel-band);
    font-size: 9.5px; color: var(--text-dim);
  }
  .panel-head span, .row span { position: absolute; }
  .row { position: absolute; left: 0; width: 100%; height: 50px; }
  .coin-icon { left: 14px; top: 12px; width: 24px; height: 24px; }
  .coin { left: 48px; top: 15px; font-size: 13px; }
  .price { right: 128px; top: 7px; font-size: 12.5px; text-align: right; }
  .change { right: 128px; top: 27px; font-size: 9px; display: flex; align-items: center; gap: 3px; }
  .change i { width: 8px; height: 8px; border-radius: 50%; display: block; }
  .up { color: var(--up); } .up i { background: var(--up); }
  .down { color: var(--down); } .down i { background: var(--down); }
  .holding { right: 14px; top: 7px; font-size: 12.5px; text-align: right; }
  .qty { right: 14px; top: 27px; font-size: 9px; color: var(--text-soft); }

  .nav {
    left: 0; top: 680px; width: 351px; height: 80px; background: var(--nav);
  }
  .nav-marker { position: absolute; left: 32px; top: 0; width: 24px; height: 2px; background: #fff; border-radius: 1px; }
  .nav-item {
    position: absolute; top: 10px; width: 80px; display: flex; flex-direction: column; align-items: center; gap: 4px;
    font-size: 9px; color: var(--text-dim);
  }
  .nav-item.active { color: #fff; font-weight: 600; }
  .home-bar { position: absolute; left: 113px; top: 68px; width: 125px; height: 4px; border-radius: 2px; background: #fff; }
</style>
</head>
<body>
<main class="screen">
  <div class="hero-texture" role="img" aria-label="Dark textured background of softly lit pebble shapes"></div>

  <div class="abs status-time">9:41</div>
  <svg class="abs status-icons" width="60" height="11" viewBox="0 0 60 11" aria-hidden="true">
    <rect x="0" y="7" width="2.5" height="4" rx="0.5" fill="#fff"/>
    <rect x="4" y="5" width="2.5" height="6" rx="0.5" fill="#fff"/>
    <rect x="8" y="3" width="2.5" height="8" rx="0.5" fill="#fff"/>
    <rect x="12" y="0.5" width="2.5" height="10.5" rx="0.5" fill="#fff"/>
    <path d="M19 4.2a8 8 0 0 1 11 0M21 6.4a5 5 0 0 1 7 0" stroke="#fff" stroke-width="1.5" fill="none" stroke-linecap="round"/>
    <circle cx="24.5" cy="9" r="1.3" fill="#fff"/>
    <rect x="36" y="1" width="20" height="9" rx="2.5" stroke="#fff" stroke-width="1" fill="none"/>
    <rect x="37.5" y="2.5" width="17" height="6" rx="1.5" fill="#fff"/>
  </svg>

  <div class="abs brand">PeZ</div>
  <svg class="abs bell" width="22" height="24" viewBox="0 0 22 24" aria-hidden="true">
    <path d="M4 17V11a7 7 0 0 1 14 0v6l2 2H2z" fill="none" stroke="#fff" stroke-width="1.6" stroke-linejoin="round"/>
    <path d="M8.5 21a2.5 2.5 0 0 0 5 0" fill="none" stroke="#fff" stroke-width="1.6"/>
  </svg>
  <div class="abs badge">8</div>
  <div class="abs avatar" role="img" aria-label="Profile photo of the account holder"></div>

  <div class="abs greeting">Hey Marlo,</div>
  <div class="abs greeting-big">Good morning!</div>

  <section class="abs card">
    <div class="card-icon">
      <svg width="18" height="14" viewBox="0 0 18 14" aria-hidden="true"><rect x="1" y="1" width="16" height="12" rx="2" fill="none" stroke="#fff" stroke-width="1.6"/><line x1="1" y1="5" x2="17" y2="5" stroke="#fff" stroke-width="1.6"/></svg>
    </div>
    <div class="card-name">Marlo Vesten</div>
    <div class="card-type">IBAN ACCOUNT</div>
    <div class="card-label">AVAILABLE BALANCE</div>
    <div class="card-balance">$10,078.04</div>
    <div class="card-number">•••• &nbsp;•••• &nbsp;0268</div>
  </section>
  <section class="abs card peek">
    <div class="card-icon">
      <svg width="18" height="14" viewBox="0 0 18 14" aria-hidden="true"><rect x="1" y="1" width="16" height="12" rx="2" fill="none" stroke="#fff" stroke-width="1.6"/><line x1="1" y1="5" x2="17" y2="5" stroke="#fff" stroke-width="1.6"/></svg>
    </div>
    <div class="card-label">AVAILABLE</div>
    <div class="card-balance">$5,</div>
  </section>
  <div class="abs pager"><span class="on"></span><span></span><span></span></div>

  <div class="abs section-title"><i></i>Top Used Functions</div>

  <div class="abs tile" style="left:15px">
    <svg width="26" height="26" viewBox="0 0 26 26" aria-hidden="true" fill="none" stroke="#e6e6e6" stroke-width="1.6">
      <rect x="2" y="2" width="8" height="8" rx="1"/><rect x="16" y="2" width="8" height="8" rx="1"/><rect x="2" y="16" width="8" height="8" rx="1"/>
      <rect x="5" y="5" width="2" height="2" fill="#e6e6e6"/><rect x="19" y="5" width="2" height="2" fill="#e6e6e6"/><rect x="5" y="19" width="2" height="2" fill="#e6e6e6"/>
      <path d="M15 15h3v3h-3zM21 15h3M15 21h3v3M21 19v5h3" />
    </svg>
    <span>Pay QR</span>
  </div>
  <div class="abs tile" style="left:98px">
    <svg width="26" height="26" viewBox="0 0 26 26" aria-hidden="true" fill="none" stroke="#e6e6e6" stroke-width="1.6" stroke-linejoin="round">
      <path d="M3 4v8l11 11 9-9L12 3H4z"/><circle cx="8" cy="8" r="1.6"/>
    </svg>
    <span>Promos &amp;<br>Discounts</span>
  </div>
  <div class="abs tile" style="left:181px">
    <svg width="26" height="26" viewBox="0 0 26 26" aria-hidden="true" fill="none" stroke="#e6e6e6" stroke-width="1.6" stroke-linecap="round">
      <path d="M4 11a9 9 0 0 1 16-4M22 15a9 9 0 0 1-16 4"/><path d="M20 3v4h-4M6 23v-4h4"/>
      <path d="M15.5 10c-.5-1-1.5-1.5-2.5-1.5-1.5 0-2.5.8-2.5 2s1 1.7 2.5 2 2.5.9 2.5 2-1 2-2.5 2c-1 0-2-.5-2.5-1.5M13 7v12"/>
    </svg>
    <span>FX Rates</span>
  </div>
  <div class="abs tile" style="left:265px">
    <svg width="26" height="26" viewBox="0 0 26 26" aria-hidden="true" fill="none" stroke="#e6e6e6" stroke-width="1.6" stroke-linejoin="round">
      <path d="M4 2h14v12M4 2v20l2-1.5 2 1.5 2-1.5 2 1.5"/><path d="M7 7h8M7 11h5M7 15h4"/>
      <path d="M14 18h4l3-2 3 2v6h-10z"/>
    </svg>
    <span>Pay Bills</span>
  </div>

  <section class="abs panel">
    <div class="panel-title">Crypto Assets Exchange</div>
    <div class="panel-date">8 OCT 2021</div>
    <div class="panel-head">
      <span style="left:14px;top:7px">COIN</span>
      <span style="left:146px;top:7px">PRICE</span>
      <span style="right:14px;top:7px">HOLDINGS</span>
    </div>
    <div class="row" style="top:90px">
      <svg class="coin-icon abs" viewBox="0 0 24 24" aria-hidden="true"><circle cx="12" cy="12" r="12" fill="#cfcfcf"/></svg>
      <span class="coin">BTC</span>
      <span class="price">$4,205.60</span>
      <span class="change up">+4.70%<i></i></span>
      <span class="holding">$40,205.60</span>
      <span class="qty">10</span>
    </div>
    <div class="row" style="top:147px">
      <svg class="coin-icon abs" viewBox="0 0 24 24" aria-hidden="true"><rect x="5" y="5" width="14" height="14" fill="#8a8a8a"/></svg>
      <span class="coin">ETH</span>
      <span class="price">$308.54</span>
      <span class="change down">-10.36%<i></i></span>
      <span class="holding">$37,024.40</span>
      <span class="qty">120</span>
    </div>
  </section>

  <nav class="abs nav">
    <div class="nav-marker"></div>
    <div class="nav-item active" style="left:4px">
      <svg width="20" height="20" viewBox="0 0 20 20" aria-hidden="true" fill="none" stroke="#fff" stroke-width="1.6"><rect x="1" y="1" width="7" height="7" rx="1"/><rect x="12" y="1" width="7" height="7" rx="1"/><rect x="1" y="12" width="7" height="7" rx="1"/><rect x="12" y="12" width="7" height="7" rx="1"/></svg>
      <span>Dashboard</span>
    </div>
    <div class="nav-item" style="left:92px">
      <svg width="20" height="20" viewBox="0 0 20 20" aria-hidden="true" fill="none" stroke="#8c8c8c" stroke-width="1.5" stroke-linejoin="round"><path d="M3 1h9l5 5v13H3z"/><path d="M12 1v5h5M7 12l2 2 4-4"/></svg>
      <span>Planning</span>
    </div>
    <div class="nav-item" style="left:180px">
      <svg width="20" height="20" viewBox="0 0 20 20" aria-hidden="true" fill="none" stroke="#8c8c8c" stroke-width="1.5" stroke-linejoin="round"><rect x="2" y="6" width="16" height="4"/><path d="M3 10v9h14v-9M10 6v13M10 6C8 2 5 2 5 4s3 2 5 2c2 0 5 0 5-2s-3-2-5 2"/></svg>
      <span>Shop Offers</span>
    </div>
    <div class="nav-item" style="left:268px">
      <svg width="20" height="20" viewBox="0 0 20 20" aria-hidden="true" fill="#8c8c8c"><circle cx="4" cy="10" r="1.7"/><circle cx="10" cy="10" r="1.7"/><circle cx="16" cy="10" r="1.7"/></svg>
      <span>More</span>
    </div>
    <div class="home-bar"></div>
  </nav>
</main>
</body>
</html>
```